Providing Back Office Solutions to Financial Advisors and Attorney Needs a Business Card Design

Need a Business Card Design that speaks to Financial Advisor and Attorneys. Some of the word that come to mind is Clean/Simple & Futuristic.

Industry/Entity Type

Business

```html
<!DOCTYPE html>
<html lang="en">
<head>
<meta charset="utf-8">
<title>Veramont Back Office Solutions – Business Card</title>
<link href="https://fonts.googleapis.com/css2?family=Open+Sans:wght@400;600;700&display=swap" rel="stylesheet">
<style>
  :root {
    --page-bg: #e6e8eb;
    --card-bg: #f7f8f9;
    --card-edge: #c9ccd1;
    --brand-blue: #1f5fa8;
    --brand-navy: #1d2b55;
    --text-dark: #2a2d33;
  }
  html, body {
    margin: 0;
    width: 1200px;
    height: 970px;
    overflow: hidden;
    background: var(--page-bg);
    font-family: "Open Sans", Arial, sans-serif;
  }
  .card {
    position: absolute;
    left: 100px;
    top: 207px;
    width: 1000px;
    height: 555px;
    box-sizing: border-box;
    background: var(--card-bg);
    border: 1.5px solid var(--card-edge);
    border-radius: 24px;
    color: var(--text-dark);
  }
  .brand {
    position: absolute;
    left: 53px;
    top: 72px;
    display: flex;
    align-items: center;
    gap: 18px;
  }
  .brand-square {
    width: 56px;
    height: 56px;
    background: var(--brand-blue);
  }
  .brand-name {
    font-size: 34px;
    font-weight: 600;
    color: var(--brand-blue);
    line-height: 1.15;
    letter-spacing: 1px;
  }
  .brand-name span { display: block; font-size: 22px; letter-spacing: 0.5px; }
  .person {
    position: absolute;
    left: 53px;
    top: 255px;
  }
  .person-name {
    margin: 0;
    font-size: 29px;
    font-weight: 700;
    color: var(--brand-navy);
    letter-spacing: 0.5px;
  }
  .person-role {
    margin: 2px 0 0;
    font-size: 22px;
  }
  .address {
    position: absolute;
    left: 53px;
    top: 346px;
    font-size: 23px;
    line-height: 32px;
    font-style: normal;
  }
  .contacts {
    position: absolute;
    left: 53px;
    top: 426px;
    margin: 0;
    padding: 0;
    list-style: none;
    font-size: 23px;
    line-height: 30px;
  }
  .contacts li { display: flex; align-items: center; gap: 10px; }
  .contacts svg { width: 20px; height: 20px; fill: var(--brand-navy); }
  .feature-mark {
    position: absolute;
    left: 560px;
    top: 60px;
    width: 400px;
    height: 440px;
    display: flex;
    flex-direction: column;
    align-items: center;
    justify-content: center;
    gap: 22px;
  }
  .feature-square {
    width: 150px;
    height: 150px;
    background: var(--brand-blue);
  }
  .feature-name {
    font-size: 56px;
    font-weight: 600;
    color: var(--brand-blue);
    letter-spacing: 3px;
  }
</style>
</head>
<body>
  <main class="card">
    <div class="brand">
      <div class="brand-square"></div>
      <div class="brand-name">VERAMONT<span>BACK OFFICE SOLUTIONS</span></div>
    </div>

    <div class="person">
      <h1 class="person-name">MARTIN HALE</h1>
      <p class="person-role">Founder / CEO</p>
    </div>

    <address class="address">
      Level 12, 40 Marlow Place<br>
      Eastvale, 20, New South Wales
    </address>

    <ul class="contacts">
      <li>
        <svg viewBox="0 0 24 24" aria-hidden="true"><path d="M3 8c0-2 4-4 9-4s9 2 9 4v2h-4V8c-1-1-3-1-5-1s-4 0-5 1v2H3zM6 11h12l3 9H3z"/></svg>
        +0 000 000 000
      </li>
      <li>
        <svg viewBox="0 0 24 24" aria-hidden="true"><path d="M2 5h20v14H2zm2 2v.5l8 5 8-5V7z"/></svg>
        martin@veramontbackoffice.com
      </li>
      <li>
        <svg viewBox="0 0 24 24" aria-hidden="true"><path d="M12 2a10 10 0 1 0 0 20 10 10 0 0 0 0-20zm0 2c1.5 1.8 2.4 4.5 2.5 7h-5C9.6 8.5 10.5 5.8 12 4zM4.1 13h3.4c.1 2.3.8 4.6 1.9 6.4A8 8 0 0 1 4.1 13zm0-2a8 8 0 0 1 5.3-6.4C8.3 6.4 7.6 8.7 7.5 11zm7.9 9c-1.5-1.8-2.4-4.5-2.5-7h5c-.1 2.5-1 5.2-2.5 7zm2.6-.6c1.1-1.8 1.8-4.1 1.9-6.4h3.4a8 8 0 0 1-5.3 6.4zm1.9-8.4c-.1-2.3-.8-4.6-1.9-6.4A8 8 0 0 1 19.9 11z"/></svg>
        www.veramontbackoffice.com
      </li>
    </ul>

    <div class="feature-mark">
      <div class="feature-square"></div>
      <div class="feature-name">VERAMONT</div>
    </div>
  </main>
</body>
</html>
```